Flyer for photo scanning business

Hello,
I need a flyer created for my business that would be suitable for print, to drop in letterboxes in my local community.

I would like the flyer to convey very simply the services I offer which is scanning negatives, slides and VHS tapes to digital files.
Hopefully it can make it look like an easy process, as people are often daunted by the task of sorting through old photos so they don't always get around to having them scanned.

I have a pinned facebook post that can be used by the designer to reference my services. Pricing does not need to be included on the flyer.
http://facebook.com/brightvaleimaging

Target Market(s)

Parents & Grandparents

Requirements
Must have
• Must make my services look simple! Refer to pinned facebook post for detailed outline of my services.

I would like to flyer to point towards my contact details -
www.brightvale.com
Margot 0478 219 836

Colours in line with my logo/brand (uploaded to brief).
Nice to have
• Stock images of 35mm film negatives, 8mm film, VHS tapes, or Lumavert slides would be worth including. I have also uploaded a mockup of the USB sticks that I provide with digitised images.
Should not have
• no prices needed,

```html
<!DOCTYPE html>
<html lang="en">
<head>
<meta charset="utf-8">
<title>Brightvale Imaging – Scanning Flyer</title>
<link rel="stylesheet" href="https://fonts.googleapis.com/css2?family=Itim&display=swap">
<style>
  :root {
    --sky: #6cb3df;
    --ink: #070707;
    --ink-soft: #2b2b2b;
    --paper: #ffffff;
    --brand-blue: #3f86c4;
    --page: #ffffff;
    --wood-a: #b5683a;
    --wood-b: #7a3f1f;
    --film-a: #c4703a;
    --film-b: #5e2a15;
    --reel-a: #283250;
    --reel-b: #0f1426;
    --slide-a: #f0c21c;
    --slide-b: #c98a12;
    --usb-a: #7fa9d4;
    --usb-b: #3e6c9e;
  }
  * { box-sizing: border-box; margin: 0; padding: 0; }
  html, body {
    width: 1200px; height: 910px; overflow: hidden;
    background: var(--page);
    font-family: "Itim", "Comic Sans MS", sans-serif;
  }
  .flyer {
    position: absolute; left: 296px; top: 25px;
    width: 608px; height: 860px;
    background: var(--sky); overflow: hidden;
  }
  .header-band {
    position: absolute; left: 0; top: 0; width: 100%; height: 219px;
    background: radial-gradient(ellipse 55% 80% at 55% 0%, var(--ink-soft), var(--ink) 70%);
  }
  .brand {
    position: absolute; left: 20px; top: 44px; width: 200px;
    text-align: center; color: var(--paper);
  }
  .brand-dot {
    width: 46px; height: 46px; border-radius: 50%;
    background: var(--brand-blue); margin: 0 auto 22px;
  }
  .brand-name {
    font-size: 23px; letter-spacing: 4px; line-height: 1.25;
  }
  .photo-frame {
    position: absolute; border: 2px solid var(--paper);
  }
  .photo { position: absolute; }
  .hero-frame { left: 242px; top: 66px; width: 349px; height: 237px; }
  .hero-photo {
    left: 253px; top: 73px; width: 331px; height: 221px;
    background: linear-gradient(135deg, var(--wood-a), var(--wood-b) 60%, #e9e2cf 100%);
  }
  .services-frame {
    position: absolute; left: 17px; top: 273px; width: 213px; height: 495px;
    border: 2px solid var(--paper);
  }
  .services-tab {
    position: absolute; left: 15px; top: 252px; width: 198px; height: 42px;
    background: var(--ink); color: var(--paper);
    border-radius: 12px 12px 12px 12px;
    display: flex; align-items: center; justify-content: center;
    font-size: 19px;
  }
  .services-list {
    position: absolute; left: 26px; top: 305px; color: var(--ink);
  }
  .services-list h2 { font-weight: 400; font-size: 19px; }
  .services-list ul { margin-left: 32px; font-size: 16px; line-height: 19.5px; }
  .media-strip { position: absolute; left: 23px; top: 417px; width: 200px; height: 342px; }
  .media-strip .photo { position: relative; width: 100%; height: 114px; }
  .film-photo { background: linear-gradient(120deg, #e6d2b8, var(--film-a) 35%, var(--film-b)); }
  .reel-photo { background: linear-gradient(160deg, #6a7088, var(--reel-a) 40%, var(--reel-b)); }
  .slide-photo { background: linear-gradient(180deg, var(--slide-a), var(--slide-b) 70%, #eee6d6); }
  .quote {
    position: absolute; left: 292px; top: 335px; width: 300px;
    text-align: center; font-size: 25px; line-height: 34px; color: var(--ink);
  }
  .usb-frame { left: 265px; top: 495px; width: 360px; height: 275px; border-right: none; }
  .usb-panel {
    position: absolute; left: 276px; top: 508px; width: 340px; height: 249px;
    background: var(--ink);
  }
  .usb-photo {
    left: 320px; top: 538px; width: 255px; height: 160px;
    background: radial-gradient(ellipse at 50% 40%, var(--usb-a), var(--usb-b));
  }
  .usb-note {
    position: absolute; left: 286px; top: 703px; width: 320px;
    color: var(--paper); font-size: 17.5px; line-height: 24px; text-align: center;
  }
  .contact-pill {
    position: absolute; left: 26px; top: 786px; width: 556px; height: 54px;
    border: 2px solid var(--paper); border-radius: 14px;
  }
  .contact-block {
    position: absolute; left: 26px; top: 786px; width: 249px; height: 54px;
    background: var(--ink); color: var(--paper); border-radius: 14px;
    text-align: center; padding-top: 6px;
  }
  .contact-web { font-size: 14px; line-height: 18px; }
  .contact-phone { font-size: 16.5px; line-height: 22px; letter-spacing: 0.5px; }
  .contact-phone svg, .contact-email svg { vertical-align: -2px; margin-right: 6px; }
  .contact-email {
    position: absolute; left: 292px; top: 803px;
    font-size: 16px; color: var(--ink);
  }
</style>
</head>
<body>
<main class="flyer">
  <div class="header-band"></div>

  <div class="brand">
    <div class="brand-dot"></div>
    <div class="brand-name">BRIGHTVALE<br>IMAGING</div>
  </div>

  <div class="photo-frame hero-frame"></div>
  <div class="photo hero-photo" role="img" aria-label="Old VHS tapes in cardboard sleeves on a wooden table"></div>

  <div class="services-frame"></div>
  <div class="services-tab">Services Offered:</div>
  <section class="services-list">
    <h2>SCANS</h2>
    <ul>
      <li>35 mm film negatives</li>
      <li>8 mm film</li>
      <li>VHS tapes</li>
      <li>Lumavert Slides</li>
    </ul>
  </section>

  <div class="media-strip">
    <div class="photo film-photo" role="img" aria-label="Strips of 35 mm film negatives"></div>
    <div class="photo reel-photo" role="img" aria-label="A pile of 8 mm film cartridges"></div>
    <div class="photo slide-photo" role="img" aria-label="Mounted Lumavert slides in a yellow box"></div>
  </div>

  <p class="quote">“ Images that haven’t been seen in years are digitised and brought back to life to enjoy again. ”</p>

  <div class="photo-frame usb-frame"></div>
  <div class="usb-panel"></div>
  <div class="photo usb-photo" role="img" aria-label="Two swivel USB sticks on a blue background"></div>
  <p class="usb-note">• &nbsp;With provided USB sticks<br>for copies of digitised images.</p>

  <div class="contact-pill"></div>
  <div class="contact-block">
    <div class="contact-web">www.brightvale.com</div>
    <div class="contact-phone">
      <svg width="12" height="14" viewBox="0 0 12 14"><path d="M3 1 L5 4 L3.5 5.5 Q5 9 7.5 10.5 L9 9 L11.5 11 L10 13 Q4 12 1.5 3 Z" fill="#fff"/></svg>0478 219 836
    </div>
  </div>
  <div class="contact-email">
    <svg width="16" height="12" viewBox="0 0 16 12"><rect x="1" y="1" width="14" height="10" fill="none" stroke="#070707" stroke-width="1.4"/><path d="M1 1 L8 7 L15 1 M1 11 L6 5.5 M15 11 L10 5.5" fill="none" stroke="#070707" stroke-width="1.2"/></svg>Margot@brightvaleimaging.com
  </div>
</main>
</body>
</html>
```